Architecture office 10 pages brochure for investors

We need a multi-page brochure (10pg) for our small architectural office.
After the long real estate crisis in Greece we're intend to reborn our architectural planning services, to relocate our targets and to communicate the philosophy in the new era of commercial buildings:
Modern architectural language, Highly energy efficient buildings with green and passive oriented design and functional details. Multifamily housing, Office buildings, Hotels, Refurbishment and Interiors from a group of new architects collaborators and an experienced leader.
We need fresh, clever styling with minimal expression and reach meanings. Written in two languages (ENG-GR) the fonts must be compatible. The solution of an digital and non-printed brochure, for on-line sharing, its a possibility and maybe unlock animated and / or AR solutions. The green color -as attached- will be appreciated.

Please provide your professional opinion about the set up of the pages.
An idea given: minimal frontpage, 2-3nd pages "about us" and "contents with photo and some minor text, and every next page refers one selected project with photo and some text for two languages (4-7 pages projects), pages 8-9 listed works-projects, collaborators, clients.
Updates

low design entries -one entry as 4 projects- , low quality, not satisfying the wills

Target Market(s)

investors in commercial buildings, private clients, energy efficiency

Industry/Entity Type

Architecture

Font styles to use
Sans Serif
Other font styles liked:
• greek compatible

Requirements
Must have
• clear - minimal design, photos, illustrations, text, contents.
• some of the projects can find them in attached link,
Nice to have
• dynamic lines, hand drawing sketches
• maybe the building design process: thoughts, sketch, hand design, cad, collaboration with other engineers, 3d renderings, animations ....
Should not have
• art deco, romantic styles, full red or basic contrasting colors (red/green, purple/orange etc)

```html
<!DOCTYPE html>
<html lang="en">
<head>
<meta charset="utf-8">
<title>About Us – Brochure Spread</title>
<link href="https://fonts.googleapis.com/css2?family=Josefin+Sans:wght@400;600;700&display=swap" rel="stylesheet">
<style>
  :root {
    --backdrop: #a4a4a4;
    --paper: #ffffff;
    --paper-shade: #e9e9e9;
    --ink: #2b2b2b;
    --ink-soft: #555555;
    --accent: #a3682f;
    --rule: #6d6d6d;
    --sand: #dcc09c;
    --sand-light: #e8d5bb;
    --sketch-a: #f1e9df;
    --sketch-b: #e3d3c0;
  }
  * { box-sizing: border-box; margin: 0; padding: 0; }
  html, body {
    width: 1200px; height: 900px; overflow: hidden;
    background: var(--backdrop);
    font-family: "Josefin Sans", sans-serif;
    color: var(--ink);
  }
  .spread {
    position: absolute;
    left: 40px; top: 250px;
    width: 1120px; height: 400px;
    display: flex;
    box-shadow: 0 18px 40px rgba(0,0,0,0.25);
  }
  .page {
    position: relative;
    width: 560px; height: 400px;
    background: var(--paper);
    overflow: hidden;
  }
  .page--left { background: linear-gradient(to right, var(--paper) 88%, var(--paper-shade)); }
  .page--right { background: linear-gradient(to left, var(--paper) 88%, var(--paper-shade)); }

  .top-rule {
    position: absolute; left: 70px; right: 30px; top: 80px;
    height: 1px; background: var(--rule);
  }
  .section-title {
    position: absolute; left: 62px; top: 100px;
    font-size: 22px; font-weight: 700; letter-spacing: 4px;
    color: var(--accent);
    padding-bottom: 3px;
    border-bottom: 1px solid var(--accent);
  }
  .columns {
    position: absolute; left: 62px; top: 135px; width: 420px;
    display: flex; gap: 24px;
  }
  .column { flex: 1; }
  .column--offset { margin-top: -20px; }
  .column-heading {
    font-size: 8px; font-weight: 700; letter-spacing: 1px;
    color: var(--accent); margin-bottom: 4px;
  }
  .column p {
    font-size: 7.4px; line-height: 1.55; color: var(--ink-soft);
    margin-bottom: 6px; text-align: justify;
  }
  .studio-mark {
    position: absolute; left: 62px; bottom: 32px;
    display: flex; align-items: center; gap: 7px;
  }
  .studio-mark__square { width: 18px; height: 18px; background: var(--ink); }
  .studio-mark__name { font-size: 10px; font-weight: 600; letter-spacing: 1px; color: var(--ink); }

  .sand-band {
    position: absolute; top: 0; right: 0; bottom: 0; width: 122px;
    background: linear-gradient(to bottom, var(--sand-light), var(--sand));
  }
  .building-sketch {
    position: absolute; left: 50px; top: 70px; width: 340px; height: 270px;
    background: radial-gradient(ellipse at 55% 45%, var(--sketch-b), var(--sketch-a) 70%, var(--paper) 100%);
  }
</style>
</head>
<body>
  <main class="spread">
    <section class="page page--left">
      <div class="top-rule"></div>
      <h1 class="section-title">ABOUT US</h1>
      <div class="columns">
        <div class="column">
          <h2 class="column-heading">WHO</h2>
          <p>Since our founding in Athens, our studio has shaped homes, offices and hotels with a modern language, clear forms and careful detail for every site and every client we serve.</p>
          <p>Today a group of young architects works beside an experienced leader, joining sketch, drawing, model and render into one open process that keeps each project calm, efficient and built to last for decades.</p>
        </div>
        <div class="column column--offset">
          <h2 class="column-heading">OUR</h2>
          <p>We design buildings that use little energy, follow the sun and wind, and give people bright, healthy rooms to live and work in.</p>
          <p>Passive strategies, green roofs and smart details guide every plan, from multifamily housing and offices to hotels, refurbishment and interiors across Greece.</p>
        </div>
      </div>
      <div class="studio-mark">
        <span class="studio-mark__square"></span>
        <span class="studio-mark__name">LITHOS STUDIO</span>
      </div>
    </section>
    <section class="page page--right">
      <div class="sand-band"></div>
      <div class="building-sketch" role="img" aria-label="Hand-drawn perspective sketch of a modern multi-storey building with curved balconies"></div>
    </section>
  </main>
</body>
</html>
```